Kestrel Property Management email template

Looking for an email template for communications sent to residents that reads well in most email formats including mobile devices. Similar to the attached email, not quite reclaimed wood but something warm with interesting texture

```html
<!DOCTYPE html>
<html lang="en">
<head>
<meta charset="utf-8">
<title>Kestrel Property Management – Fall Preparation Email</title>
<link href="https://fonts.googleapis.com/css2?family=Roboto:wght@400;500;700&display=swap" rel="stylesheet">
<style>
  :root {
    --navy: #14204a;
    --sky: #94b6e0;
    --white: #ffffff;
    --page: #eceef4;
    --stone-light: #eeeff1;
    --stone-mid: #d3d5d9;
    --photo-warm: #e9d6c4;
    --photo-light: #f3efea;
    --photo-roof: #c9583f;
  }
  * { box-sizing: border-box; margin: 0; padding: 0; }
  html, body {
    width: 1200px; height: 1200px; overflow: hidden;
    background: var(--page);
    font-family: "Roboto", Arial, sans-serif;
  }
  .canvas { position: relative; width: 1200px; height: 1200px; }
  .stone-backdrop {
    position: absolute; left: 98px; top: 1px; width: 1003px; height: 1197px;
    background:
      radial-gradient(ellipse at 20% 30%, var(--stone-mid) 0%, transparent 45%),
      radial-gradient(ellipse at 85% 70%, var(--stone-mid) 0%, transparent 40%),
      linear-gradient(135deg, var(--stone-light), #dfe1e4 50%, var(--stone-light));
  }
  .email-card {
    position: absolute; left: 166px; top: 42px; width: 671px; height: 1113px;
    background: var(--white); border: 2px solid var(--navy); overflow: hidden;
  }
  .brand {
    position: absolute; top: 52px; left: 0; width: 100%;
    display: flex; justify-content: center; align-items: center; gap: 14px;
  }
  .brand-mark { width: 40px; height: 40px; background: var(--navy); }
  .brand-name {
    color: var(--navy); font-weight: 700; font-size: 26px; line-height: 1.15;
    letter-spacing: 0.5px;
  }
  .sky-band {
    position: absolute; left: 0; top: 267px; width: 100%; height: 503px;
    background: var(--sky);
  }
  .hero-photo {
    position: absolute; left: 72px; top: 176px; width: 527px; height: 412px;
    border: 12px solid var(--navy);
    background:
      radial-gradient(ellipse at 50% 45%, var(--photo-roof) 0%, transparent 28%),
      radial-gradient(ellipse at 50% 85%, var(--photo-warm) 0%, transparent 55%),
      linear-gradient(180deg, #e4e0da, var(--photo-light));
  }
  .headline {
    position: absolute; top: 608px; left: 0; width: 100%;
    text-align: center; font-size: 29px; line-height: 35px; color: var(--white);
  }
  .headline strong { display: block; color: var(--navy); font-weight: 700; }
  .thumb-row { position: absolute; top: 700px; left: 50px; display: flex; gap: 18px; }
  .thumb {
    width: 178px; height: 139px; border: 3px solid var(--navy);
    background:
      radial-gradient(ellipse at 50% 45%, var(--photo-roof) 0%, transparent 30%),
      radial-gradient(ellipse at 50% 90%, var(--photo-warm) 0%, transparent 55%),
      linear-gradient(180deg, #e4e0da, var(--photo-light));
  }
  .tagline {
    position: absolute; top: 860px; left: 0; width: 100%;
    text-align: center; font-size: 25px; color: var(--navy);
  }
  .call-bar {
    position: absolute; top: 902px; left: 0; width: 100%; height: 48px;
    background: var(--navy); color: var(--white);
    font-size: 29px; font-weight: 500; line-height: 48px; text-align: center;
  }
  .service-list {
    position: absolute; top: 976px; left: 99px; list-style: none;
    font-size: 21px; line-height: 32px; color: var(--navy);
  }
  .service-list li::before {
    content: "•"; color: var(--sky); margin-right: 10px;
  }
</style>
</head>
<body>
<div class="canvas">
  <div class="stone-backdrop" role="img" aria-label="Grey marble texture with gold veining"></div>
  <div class="email-card">
    <div class="brand">
      <span class="brand-mark"></span>
      <span class="brand-name">Kestrel Property<br>Management</span>
    </div>
    <div class="sky-band"></div>
    <div class="hero-photo" role="img" aria-label="Hands holding a small model house with a red roof"></div>
    <p class="headline">Fal maintenance and preparation key to <strong>peace of mind come winter.</strong></p>
    <div class="thumb-row">
      <div class="thumb" role="img" aria-label="Hands holding a model house"></div>
      <div class="thumb" role="img" aria-label="Hands holding a model house"></div>
      <div class="thumb" role="img" aria-label="Hands holding a model house"></div>
    </div>
    <p class="tagline">“They” are saying it’s going to be a tough one.</p>
    <div class="call-bar">Let us help you be prepared (and at peace)!</div>
    <ul class="service-list">
      <li>HVAC Preventative Maintenance and Servicing</li>
      <li>Roof and gutter once-overs for proper run off</li>
    </ul>
  </div>
</div>
</body>
</html>
```